Business Card *

A business card design
Use the logo uploaded in the brief page.
You may use placeholders in your design layouts.
I will provide the actual business card details to the winning designer.

Logo
Place for contact info (name, title, phone, email, etc)

Requirements
Must have
• Logo

```html
<!DOCTYPE html>
<html lang="en">
<head>
<meta charset="utf-8">
<title>Holloway Business Card</title>
<link href="https://fonts.googleapis.com/css2?family=Montserrat:wght@800&family=Roboto:wght@300;400;500&display=swap" rel="stylesheet">
<style>
  :root {
    --green: #3bb54a;
    --lime: #8cc63f;
    --grey: #8a8a8a;
    --ink: #6d6e71;
    --white: #ffffff;
    --backdrop: #ececec;
  }
  * { margin: 0; padding: 0; box-sizing: border-box; }
  html, body { width: 1200px; height: 912px; overflow: hidden; }
  body {
    background: var(--backdrop);
    font-family: "Roboto", Arial, sans-serif;
    position: relative;
  }
  .card {
    position: absolute;
    width: 560px;
    height: 320px;
    border-radius: 18px;
    overflow: hidden;
    box-shadow: 0 12px 30px rgba(0,0,0,0.18);
  }
  .card-front {
    left: 60px; top: 80px;
    background: var(--green);
    display: flex; align-items: center; justify-content: center;
  }
  .card-back {
    left: 580px; top: 510px;
    background: var(--white);
  }
  .brand {
    display: flex; align-items: center; gap: 14px;
    font-family: "Montserrat", Arial, sans-serif;
    font-weight: 800;
    letter-spacing: 1px;
  }
  .brand-mark { border-radius: 50%; flex: none; }
  .card-front .brand { font-size: 46px; color: var(--white); }
  .card-front .brand-mark { width: 38px; height: 38px; border: 5px solid var(--white); }
  .card-back .brand {
    position: absolute; left: 40px; top: 120px;
    font-size: 32px; color: var(--grey);
  }
  .card-back .brand-mark { width: 28px; height: 28px; background: var(--green); }
  .wave { position: absolute; inset: 0; width: 560px; height: 320px; }
  .edge-tab {
    position: absolute; right: 0; top: 22px;
    width: 12px; height: 40px; background: var(--green);
  }
  .holder {
    position: absolute; right: 30px; top: 26px; text-align: right;
  }
  .holder-name {
    font-weight: 500; font-size: 24px; color: var(--lime); letter-spacing: -0.5px;
  }
  .holder-title { font-weight: 300; font-size: 15px; color: var(--ink); }
  .contact {
    position: absolute; right: 26px; top: 162px;
    list-style: none; text-align: right;
    color: var(--white); font-size: 15px; line-height: 21px; font-weight: 400;
  }
  .contact li { display: flex; justify-content: flex-end; align-items: center; gap: 6px; }
  .contact svg { width: 11px; height: 11px; flex: none; }
  .contact .no-icon { padding-right: 17px; }
</style>
</head>
<body>
  <section class="card card-front">
    <div class="brand"><span class="brand-mark"></span><span>HOLLOWAY</span></div>
  </section>

  <section class="card card-back">
    <svg class="wave" viewBox="0 0 560 320" aria-hidden="true">
      <path d="M560 92 C430 90 380 110 345 160 C310 215 270 300 200 320 L560 320 Z" fill="var(--green)"/>
      <path d="M560 80 C420 78 368 98 332 150 C298 205 258 292 180 320" fill="none" stroke="var(--green)" stroke-width="5"/>
      <path d="M300 175 C270 250 200 295 30 303 L30 290 C180 286 265 245 300 175 Z" fill="var(--lime)"/>
      <path d="M30 303 C200 295 270 250 300 175 C290 240 230 300 120 320 L30 320 Z" fill="var(--green)"/>
    </svg>
    <span class="edge-tab"></span>
    <div class="holder">
      <div class="holder-name">DANIEL REYES</div>
      <div class="holder-title">Director</div>
    </div>
    <div class="brand"><span class="brand-mark"></span><span>HOLLOWAY</span></div>
    <ul class="contact">
      <li class="no-icon">1427 Alder Court</li>
      <li class="no-icon">Springfield, MA 01109</li>
      <li>041 555 20 37
        <svg viewBox="0 0 12 12"><path d="M3 1l2 2-1 1.5c.6 1.3 1.3 2 2.5 2.5L8 5.5l2 2-1.5 2C5 9 3 7 2.5 3.5z" fill="var(--white)"/></svg></li>
      <li>info@hollowayag.com
        <svg viewBox="0 0 12 12"><rect x="1" y="2.5" width="10" height="7" fill="none" stroke="var(--white)" stroke-width="1.2"/><path d="M1 2.5l5 4 5-4" fill="none" stroke="var(--white)" stroke-width="1.2"/></svg></li>
      <li>www.hollowayag.com
        <svg viewBox="0 0 12 12"><circle cx="6" cy="6" r="5" fill="none" stroke="var(--white)" stroke-width="1.2"/><path d="M1 6h10M6 1c-2.5 3-2.5 7 0 10M6 1c2.5 3 2.5 7 0 10" fill="none" stroke="var(--white)" stroke-width="1"/></svg></li>
    </ul>
  </section>
</body>
</html>
```